Vantrelix Template Refresh 2017

We want software development managers to remember that presentations using this template showcased Vantrelix technology: Our template must be distinctive to be remembered as showing Vantrelix technology: They must stand out from the 100s of other tech presentations they see, without being 'wacky', but professional whether bold or subtle. We are targeting the world's largest corporations.

[What do we do?] Vantrelix offers the world's first objective, fair measure of software developer productivity (Vantrelix Keystroke Gauge) and code quality (Vantrelix DUX) metrics.

Our corporate colour is (hex) Red: 13, Green: 10, Blue: 74.

Target Market(s)

CIOs, CTOs and senior software development managers in large Enterprises.

Industry/Entity Type

Information Technology

Font styles to use
Sans Serif

Colors
0355a3

Requirements
Must have
• A memorable design
Nice to have
• Template for slides that will show a view of our User Interface (which shows graphs and charts); ideally a consistent theme to make it clear that this is our own UI, not general graphs and charts to illustrate the presentation. (None of the graphs and charts in the attached presentation are from our User Interface)
• A suggestion would be to make use of our "chord" shape (cut off circle in our logo). This could be white on a blue to appear as a cut-out window for the slide content.
Should not have
• A colourful / jokey / fun tone.

```html
<!DOCTYPE html>
<html lang="en">
<head>
<meta charset="UTF-8">
<title>Example Source Code Metrics — Vantrelix</title>
<link href="https://fonts.googleapis.com/css2?family=Source+Sans+3:wght@300;400;600;700&display=swap" rel="stylesheet">
<style>
  :root {
    --brand-navy: #25205f;
    --label-fill: #4f4c7d;
    --detail-fill: #d3d3e0;
    --ink: #2e2e2e;
    --white: #ffffff;
    --muted: #8a8a8a;
    --rule: #e2e2e2;
  }
  * { margin: 0; padding: 0; box-sizing: border-box; }
  html, body { width: 1200px; height: 675px; overflow: hidden; background: var(--white); }
  body { font-family: "Source Sans 3", "Source Sans Pro", sans-serif; position: relative; color: var(--ink); }

  .slide { position: relative; width: 1200px; height: 675px; }

  .title-band {
    position: absolute; left: 0; top: 10px; width: 1200px; height: 68px;
    background: var(--brand-navy);
  }
  .slide-title {
    position: absolute; left: 116px; top: 13px;
    font-weight: 700; font-size: 42px; line-height: 1; color: var(--white);
    letter-spacing: -0.2px;
  }
  .slide-intro {
    position: absolute; left: 118px; top: 84px;
    font-weight: 300; font-size: 14.6px; color: #333;
  }

  .metrics-table {
    position: absolute; left: 118px; top: 144px; width: 977px;
    display: grid; grid-template-columns: 333px 644px; row-gap: 2px;
  }
  .metric-name, .metric-detail {
    height: 56px; font-size: 10.8px; line-height: 13.6px; padding-top: 14px;
  }
  .metric-name {
    background: var(--label-fill); color: var(--white);
    text-align: right; padding-right: 29px;
  }
  .metric-detail {
    background: var(--detail-fill); color: var(--ink);
    padding-left: 18px;
  }

  .footer-rule {
    position: absolute; left: 0; top: 645px; width: 1200px; height: 2px;
    background: linear-gradient(var(--rule), transparent);
  }
  .brand-name {
    position: absolute; left: 66px; top: 650px;
    font-weight: 600; font-size: 18px; line-height: 1.2; color: var(--brand-navy);
  }
  .copyright {
    position: absolute; left: 0; width: 1294px; top: 655px; text-align: center;
    font-size: 7px; color: var(--muted);
  }
  .slide-number {
    position: absolute; right: 54px; top: 655px; font-size: 7px; color: var(--muted);
  }
</style>
</head>
<body>
<div class="slide">
  <header class="title-band">
    <h1 class="slide-title">Example Source Code Metrics</h1>
  </header>
  <p class="slide-intro">Examples of the types of static source code metrics that are gathered from every interaction that every developer has with source files.</p>

  <section class="metrics-table">
    <div class="metric-name">Lorem Ipsum is simply dummy text<br>of the printing and typesetting</div>
    <div class="metric-detail">Lorem Ipsum is simply dummy text of the printing and typesetting industry. Lorem Ipsum has been the industry's standard<br>dummy text ever since the 1500s, when an unknown printer took a galley of type and scrambled it to make a type specimen book.</div>

    <div class="metric-name">Lorem Ipsum is simply dummy text of the print-<br>ing and typesetting industry. Lorem Ipsum has</div>
    <div class="metric-detail">Lorem Ipsum is simply dummy text of the printing and typesetting industry. Lorem Ipsum has been the industry's standard</div>

    <div class="metric-name">Lorem Ipsum is simply dummy text<br>of the printing and typesetting</div>
    <div class="metric-detail">Lorem Ipsum is simply dummy text of the printing and typesetting industry. Lorem Ipsum has been the industry's standard<br>dummy text ever since the 1500s, when an unknown printer took a galley of type and scrambled it to make a type specimen book.</div>

    <div class="metric-name">Lorem Ipsum is simply dummy text of the print-<br>ing and typesetting industry. Lorem Ipsum has</div>
    <div class="metric-detail">Lorem Ipsum is simply dummy text of the printing and typesetting industry. Lorem Ipsum has been the industry's standard</div>

    <div class="metric-name">Lorem Ipsum is simply dummy text<br>of the printing and typesetting</div>
    <div class="metric-detail">Lorem Ipsum is simply dummy text of the printing and typesetting industry. Lorem Ipsum has been the industry's standard<br>dummy text ever since the 1500s, when an unknown printer took a galley of type and scrambled it to make a type specimen book.</div>

    <div class="metric-name">Lorem Ipsum is simply dummy text of the print-<br>ing and typesetting industry. Lorem Ipsum has</div>
    <div class="metric-detail">Lorem Ipsum is simply dummy text of the printing and typesetting industry. Lorem Ipsum has been the industry's standard</div>

    <div class="metric-name">Lorem Ipsum is simply dummy text<br>of the printing and typesetting</div>
    <div class="metric-detail">Lorem Ipsum is simply dummy text of the printing and typesetting industry. Lorem Ipsum has been the industry's standard<br>dummy text ever since the 1500s, when an unknown printer took a galley of type and scrambled it to make a type specimen book.</div>

    <div class="metric-name">Lorem Ipsum is simply dummy text of the print-<br>ing and typesetting industry. Lorem Ipsum has</div>
    <div class="metric-detail">Lorem Ipsum is simply dummy text of the printing and typesetting industry. Lorem Ipsum has been the industry's standard</div>
  </section>

  <footer>
    <div class="footer-rule"></div>
    <p class="brand-name">Vantrelix</p>
    <p class="copyright">Copyright Vantrelix Limited 2015 - 2017. All rights reserved</p>
    <p class="slide-number">Slide 01</p>
  </footer>
</div>
</body>
</html>
```